Marigold Shore Realty business card design

Looking for an upscale and clean business card design and updated logo. I sell to a very high-end south Florida real estate market.
Target Market(s)
High-end real estate in south Florida real estate market
Industry/Entity Type
Real Estate Agent
Contact Information for Business Card
Marigold Shore Realty, Inc
738 West Penrick Ave, Suite 400/500, Fort Lauderdale, FL 33315
Tim Harlow - Broker/Owner
954-327-8846 Direct
timshomes@quillmail.net
Website: StayPenrickAv.net
Font styles to use
Other font styles liked:
- Copperplate Gothic, Georgia, etc.
Requirements
Must have
- My photo, company name, my name and title, all info stated in Details above
Nice to have
- Luxury home design element, waterfront

```html
<!DOCTYPE html>
<html lang="en">
<head>
<meta charset="utf-8">
<title>Marigold Shore Realty – Business Card</title>
<link href="https://fonts.googleapis.com/css2?family=Cinzel:wght@600;700&family=Gelasio:ital,wght@0,400;1,400&display=swap" rel="stylesheet">
<style>
  :root {
    --backdrop: #ececec;
    --card-tan: #bfb38a;
    --card-black: #020202;
    --ink-white: #ffffff;
    --ink-grey: #4a4741;
    --accent-gold: #f2cc1f;
    --photo-top: #c9bd93;
    --photo-suit: #263a86;
    --photo-shirt: #f2c9d6;
  }
  * { margin: 0; padding: 0; box-sizing: border-box; }
  html, body {
    width: 1200px; height: 1200px; overflow: hidden;
    background: var(--backdrop);
  }
  .sheet {
    position: relative; width: 1200px; height: 1200px;
    display: flex; flex-direction: column; align-items: center; justify-content: center;
    gap: 60px;
  }
  .card {
    position: relative; width: 700px; height: 400px;
    box-shadow: 0 10px 30px rgba(0,0,0,0.18);
    overflow: hidden;
  }
  /* Front */
  .card--front { background: var(--card-tan); }
  .contact {
    position: absolute; left: 52px; top: 46px;
    font-family: "Gelasio", Georgia, serif;
  }
  .contact__name {
    font-family: "Cinzel", "Copperplate", serif;
    font-weight: 700; font-size: 34px; color: var(--ink-white);
    letter-spacing: 1px; line-height: 1;
  }
  .contact__title { font-size: 19px; color: var(--ink-white); margin-top: 6px; }
  .contact__lines {
    margin-top: 20px; font-size: 16px; color: var(--ink-grey);
    display: grid; grid-template-columns: auto auto; column-gap: 6px; row-gap: 4px;
  }
  .contact__company {
    margin-top: 16px; font-style: italic; font-size: 16px; color: var(--ink-grey);
  }
  .contact__address {
    margin-top: 10px; font-size: 16px; color: var(--ink-white); line-height: 1.45;
  }
  .portrait {
    position: absolute; right: 40px; bottom: 0; width: 300px; height: 330px;
    background: linear-gradient(180deg, var(--photo-top) 0%, var(--photo-shirt) 40%, var(--photo-suit) 62%, var(--photo-suit) 100%);
    border-radius: 140px 140px 0 0;
  }
  /* Back */
  .card--back {
    background: var(--card-black);
    display: flex; flex-direction: column; align-items: center; justify-content: center;
  }
  .brand__mark {
    width: 62px; height: 62px; border: 3px solid var(--accent-gold); margin-bottom: 22px;
  }
  .brand__name, .brand__sub {
    font-family: "Cinzel", "Copperplate", serif; font-weight: 600;
    color: var(--ink-white); text-align: center;
  }
  .brand__name { font-size: 38px; letter-spacing: 4px; }
  .brand__sub { font-size: 22px; letter-spacing: 6px; margin-top: 6px; }
</style>
</head>
<body>
  <main class="sheet">
    <section class="card card--front">
      <div class="contact">
        <h1 class="contact__name">Tim Harlow</h1>
        <p class="contact__title">Broker/Owner</p>
        <div class="contact__lines">
          <span>Direct :</span><span>954-327-8846</span>
          <span>Web&nbsp;&nbsp;&nbsp;&nbsp;:</span><span>StayPenrickAv.net</span>
          <span>Email :</span><span>timshomes@quillmail.net</span>
        </div>
        <p class="contact__company">Marigold Shore Realty, Inc</p>
        <p class="contact__address">738 West Penrick Ave,<br>Suite 400/500,<br>Fort Lauderdale,&nbsp; FL 33315</p>
      </div>
      <div class="portrait" role="img" aria-label="Portrait photo of the broker in a blue plaid jacket and pink shirt"></div>
    </section>

    <section class="card card--back">
      <div class="brand__mark"></div>
      <p class="brand__name">Marigold Shore</p>
      <p class="brand__sub">Realty, Inc</p>
    </section>
  </main>
</body>
</html>
```